Business Card for TOV

We need a Corporate style business card for a new Industrial recycling company based in Australia. We recycle industrial products from Mining companies, power stations and other large industry all around the country.

We want the card to represent a modern, innovative professional company that is an industry leader.

We want the card to be double sided. I think with the logo centred by itself on one side and the text displayed with all our details on the other side.

(or you could put the persons name with the job title on the side with the logo?? I'll leave that up to your creative sides)

Open to how you divide and place the information on the one side of the card.

I think the persons name and the title should have its own place. The rest of the information can be placed as you think is best and then I will provide feedback as to what I think works best.

I have attached the logo file so you can add that to the one side. Whether you use it in a smaller form on the second side too is an option but I'll leave that up to you initially?

Information required on the card is as follows

Dermot Halloran
Director

0438 972 506

dermot@tovq.com.au

Po Box 782
Brindle ACT 2694

www.tovq.com.au

ACN 582 917 306 (This can be in very small print and can be in the bottom corner of the card or somewhere not very prominent

Wanted to thank everyone for their submissions. 

We were really torn on about 5 designs in the end.

We decided to go with the first one we liked.

We have another company that is going to need logo and business card design in the coming weeks.

I will save your designer ID's so I can invite you all to that project. too!

Thanks again and all the best

Dermot

Target Market(s)

Corporate and medium to large business clients

Industry/Entity Type

Industrial

```html
<!DOCTYPE html>
<html lang="en">
<head>
<meta charset="utf-8">
<title>TOV Industrial Recyclers – Business Card</title>
<link rel="stylesheet" href="https://fonts.googleapis.com/css2?family=Open+Sans:wght@400;600;700&display=swap">
<style>
  :root {
    --backdrop: #1f1f1f;
    --card-white: #ffffff;
    --brand-green: #7dc242;
    --brand-blue: #2b9fcc;
    --brand-blue-deep: #1c6a8f;
    --ink-dark: #2e2e2e;
    --ink-muted: #555555;
    --text-light: #ffffff;
  }
  * { box-sizing: border-box; margin: 0; padding: 0; }
  html, body {
    width: 1200px; height: 1000px; overflow: hidden;
    background: var(--backdrop);
    font-family: "Open Sans", Arial, sans-serif;
  }
  .sheet {
    width: 1200px; height: 1000px;
    display: flex; flex-direction: column;
    align-items: center; justify-content: center; gap: 60px;
  }
  .card {
    position: relative;
    width: 640px; height: 390px;
    border-radius: 30px;
    overflow: hidden;
    background: var(--card-white);
    box-shadow: 0 12px 30px rgba(0,0,0,.45);
  }

  /* Brand lockup */
  .brand {
    display: flex; flex-direction: column; align-items: center; gap: 14px;
  }
  .brand__dot {
    width: 86px; height: 86px; border-radius: 50%;
    background: var(--brand-green);
  }
  .brand__name {
    font-weight: 700; color: var(--ink-dark);
    font-size: 26px; letter-spacing: 1px; text-align: center; line-height: 1.15;
  }

  /* Logo side */
  .card--logo .brand {
    position: absolute; left: 0; right: 0; top: 92px;
  }
  .card--logo .acn {
    position: absolute; right: 30px; top: 232px;
    font-size: 11px; color: var(--ink-muted);
  }

  /* Details side */
  .card--details .brand {
    position: absolute; left: 0; top: 120px; width: 290px;
  }
  .card--details .brand__dot { width: 74px; height: 74px; }
  .card--details .brand__name { font-size: 20px; }

  .details-panel {
    position: absolute; top: 0; right: 0; bottom: 0; width: 340px;
    background: linear-gradient(180deg, var(--brand-blue) 0%, var(--brand-blue-deep) 100%);
    color: var(--text-light);
  }
  .name-band {
    margin-top: 26px; height: 86px;
    background: var(--brand-green);
    padding: 14px 0 0 42px;
  }
  .name-band__name { font-size: 27px; font-weight: 400; line-height: 1.1; }
  .name-band__role { font-size: 17px; padding-left: 12px; }

  .contact-list {
    list-style: none; padding: 22px 0 0 54px;
    font-size: 17px; line-height: 1.55;
  }
  .contact-list .address { margin-top: 6px; line-height: 1.3; }
</style>
</head>
<body>
  <main class="sheet">
    <section class="card card--logo" aria-label="Business card, logo side">
      <div class="brand">
        <span class="brand__dot"></span>
        <span class="brand__name">TOV INDUSTRIAL<br>RECYCLERS</span>
      </div>
      <p class="acn">ACN 582 917 306</p>
    </section>

    <section class="card card--details" aria-label="Business card, details side">
      <div class="brand">
        <span class="brand__dot"></span>
        <span class="brand__name">TOV INDUSTRIAL<br>RECYCLERS</span>
      </div>
      <div class="details-panel">
        <div class="name-band">
          <p class="name-band__name">Dermot Halloran</p>
          <p class="name-band__role">Director</p>
        </div>
        <ul class="contact-list">
          <li>0438 972 506</li>
          <li>dermot@tovq.com.au</li>
          <li>www.tovq.com.au</li>
          <li class="address">Po Box 782<br>Brindle ACT 2694</li>
        </ul>
      </div>
    </section>
  </main>
</body>
</html>
```